Graphic Design of Business Process

We require an eye-catching, sophisticated design of 2 business processes (attached), that will be used digitally AND for print (to be put on walls in our office).

The basic layout is attached. We require a creative, professional designer to re-design these so that they look appealing but still able to grasp all the information.

We will require vector files and editable project files for final delivery. You may refer to our website (kitefieldmedia.com.au) for an indication of our brand.

If you have any questions, please ask.

Thank you.

```html
<!DOCTYPE html>
<html lang="en">
<head>
<meta charset="utf-8">
<title>Sales to Content Funnel — Kitefield Media</title>
<link rel="stylesheet" href="https://fonts.googleapis.com/css2?family=Montserrat:wght@700;800&family=Oswald:wght@400;500;600&display=swap">
<style>
  :root {
    --ink: #111111;
    --frame: #d9d5d5;
    --blue-light: #29a9e1;
    --blue-deep: #1b8fc4;
    --blue-pale: #9cc6e0;
    --blue-icon: #5cbfe9;
    --orange: #f7941d;
    --orange-deep: #ef7f22;
    --orange-pale: #f0bc82;
    --orange-icon: #f9b25c;
    --red: #ee3a45;
    --red-light: #f25e60;
    --red-pale: #e9958a;
    --red-icon: #f47b79;
    --maroon: #5a1a1e;
    --navy: #2a2f6b;
    --crimson: #b31f2a;
    --yellow: #fff03a;
    --white: #ffffff;
    --ground: #3a2417;
  }
  html, body {
    margin: 0;
    padding: 0;
    width: 1200px;
    height: 581px;
    overflow: hidden;
  }
  .funnel-board {
    display: block;
    width: 1200px;
    height: 581px;
  }
  .title {
    font-family: "Montserrat", sans-serif;
    font-weight: 800;
    font-size: 46px;
    fill: var(--ink);
  }
  .stage-name {
    font-family: "Oswald", sans-serif;
    font-weight: 600;
    fill: var(--white);
  }
  .stage-goal {
    font-family: "Oswald", sans-serif;
    font-weight: 400;
    font-size: 24px;
  }
  .stage-point {
    font-family: "Oswald", sans-serif;
    font-weight: 400;
    font-size: 16px;
    fill: var(--white);
  }
  .side-head {
    font-family: "Oswald", sans-serif;
    font-weight: 600;
    font-size: 22px;
    fill: var(--maroon);
  }
  .side-note {
    font-family: "Oswald", sans-serif;
    font-weight: 400;
    font-size: 16px;
    fill: var(--maroon);
  }
  .referral-label {
    font-family: "Oswald", sans-serif;
    font-weight: 600;
    font-size: 24px;
    fill: var(--maroon);
  }
  .referral-line {
    fill: none;
    stroke: var(--maroon);
    stroke-width: 5;
  }
  .brand-name {
    font-family: "Montserrat", sans-serif;
    font-weight: 700;
    font-size: 28px;
    letter-spacing: 4px;
    fill: var(--white);
  }
</style>
</head>
<body>
<svg class="funnel-board" viewBox="0 0 1500 726" xmlns="http://www.w3.org/2000/svg">
  <defs>
    <radialGradient id="backdrop" cx="0.85" cy="0.1" r="1.1">
      <stop offset="0" stop-color="#f7c9bf"/>
      <stop offset="0.55" stop-color="#fbe9e4"/>
      <stop offset="1" stop-color="#fdf3f0"/>
    </radialGradient>
    <marker id="arrow-tip" viewBox="0 0 10 10" refX="2" refY="5" markerWidth="4" markerHeight="4" orient="auto-start-reverse">
      <path d="M0 0 L10 5 L0 10 Z" fill="#5a1a1e"/>
    </marker>
  </defs>

  <rect class="backdrop" width="1500" height="726" fill="url(#backdrop)"/>

  <text class="title" x="750" y="106" text-anchor="middle">SALES —&gt; CONTENT FUNNEL</text>

  <!-- funnel frame -->
  <polygon class="funnel-frame" points="375,138 1107,138 1440,668 65,668" fill="var(--frame)"/>

  <!-- awareness tier -->
  <polygon class="tier-awareness-base" points="385,150 1090,150 1420,668 85,668" fill="var(--blue-light)"/>
  <polygon class="tier-awareness-side" points="800,150 1090,150 1192,310 890,310" fill="var(--blue-pale)"/>
  <polygon class="tier-awareness-band" points="385,150 800,150 890,310 478,310" fill="var(--blue-deep)"/>

  <!-- consideration tier -->
  <polygon class="tier-consideration-edge" points="470,310 478,310 300,668 240,668" fill="var(--orange-deep)"/>
  <polygon class="tier-consideration-base" points="478,310 1192,310 1420,668 270,668" fill="var(--orange)"/>
  <polygon class="tier-consideration-side" points="890,310 1192,310 1303,485 985,485" fill="var(--orange-pale)"/>

  <!-- action tier -->
  <polygon class="tier-action-base" points="575,485 985,485 1100,668 455,668" fill="var(--red)"/>
  <polygon class="tier-action-facet" points="575,485 695,668 470,668" fill="var(--red-light)"/>
  <polygon class="tier-action-side" points="985,485 1303,485 1418,668 1100,668" fill="var(--red-pale)"/>

  <!-- stage icons -->
  <rect class="icon-awareness" role="img" aria-label="Icon of a head with an idea spark" x="318" y="258" width="102" height="126" rx="28" fill="var(--blue-icon)"/>
  <rect class="icon-consideration" role="img" aria-label="Icon of a path branching into three arrows" x="400" y="438" width="124" height="116" rx="26" fill="var(--orange-icon)"/>
  <rect class="icon-action" role="img" aria-label="Icon of two hands reaching to shake" x="512" y="558" width="106" height="92" rx="14" fill="var(--red-icon)"/>

  <!-- awareness copy -->
  <text class="stage-name" x="452" y="206" font-size="48">AWARENESS</text>
  <text class="stage-goal" x="473" y="240" fill="var(--navy)">IDENTIFY PROBLEM/NEED</text>
  <text class="stage-point" x="490" y="273">- ASPIRATIONAL</text>
  <text class="stage-point" x="490" y="296">- MARKET THE OUTCOME NOT PRODUCT</text>

  <text class="side-head" x="873" y="219">PROBLEM &amp; SOLUTION</text>
  <text class="side-note" x="895" y="250">SUBJECT SHOWING</text>
  <text class="side-note" x="895" y="275">SYMPTOMS OF PROBLEM</text>

  <!-- consideration copy -->
  <text class="stage-name" x="531" y="371" font-size="52">CONSIDERATION</text>
  <text class="stage-goal" x="568" y="406" fill="var(--crimson)">EVALUATE ALTERNATIVES</text>
  <text class="stage-point" x="578" y="437">- WHY IS THIS SOLUTION BETTER THAN OTHERS</text>
  <text class="stage-point" x="578" y="463">- HOW IS THIS PROVIDER GOING TO SOLVE MY NEED</text>

  <text class="side-head" x="956" y="365">PROVIDERS &amp;</text>
  <text class="side-head" x="956" y="394">TYPES OF SOLUTION</text>
  <text class="side-note" x="973" y="424">SUBJECT GIVES NAME TO PROBLEM</text>

  <!-- action copy -->
  <text class="stage-name" x="628" y="546" font-size="48">ACTION/DECISION</text>
  <text class="stage-goal" x="662" y="585" fill="var(--yellow)" font-size="22">PRESENT AN OFFER</text>
  <text class="stage-point" x="676" y="625" font-size="15">- WHICH PROVIDER?</text>

  <text class="side-head" x="1085" y="570">CONVERT &amp; RETAIN</text>

  <!-- word of mouth loop -->
  <path class="referral-line" d="M1214 262 L1184 205 H1130" marker-end="url(#arrow-tip)"/>
  <path class="referral-line" d="M1242 350 H1168" marker-end="url(#arrow-tip)"/>
  <path class="referral-line" d="M1334 452 L1377 525 H1010" marker-end="url(#arrow-tip)"/>
  <text class="referral-label" x="1276" y="365" text-anchor="middle" transform="rotate(58 1276 357)">WOM &amp; REFERRAL</text>

  <!-- ground band -->
  <rect class="ground-band" x="0" y="668" width="1500" height="58" fill="var(--ground)"/>
  <text class="brand-name" x="1262" y="707" text-anchor="middle">KITEFIELD MEDIA</text>
</svg>
</body>
</html>
```